Business Card

We are looking to re-create our business card. Attached is the company logo. we would like it to be back and front. for example one side with the persons information and the other side with the company logo. Be as creative as you would like but also keep in mind, we are a Health Insurance company and we need to look professional as well.
Business

```html
<!DOCTYPE html>
<html lang="en">
<head>
<meta charset="utf-8">
<title>Meridian Care Partners – Business Card Concepts</title>
<link rel="stylesheet" href="https://fonts.googleapis.com/css2?family=Source+Sans+3:wght@400;600&family=Arimo&display=swap">
<style>
  :root {
    --brand-blue: #1a93d3;
    --text-grey: #8c8c8c;
    --ink: #222222;
    --card-border: #555555;
    --paper: #ffffff;
  }
  * { box-sizing: border-box; margin: 0; padding: 0; }
  html, body { width: 1018px; height: 1200px; overflow: hidden; background: var(--paper); }
  .sheet {
    position: relative; width: 1018px; height: 1200px;
    font-family: "Source Sans 3", "Myriad Pro", sans-serif;
  }
  .sheet-label {
    position: absolute; font-family: "Arimo", Arial, sans-serif;
    font-size: 13px; color: var(--ink); transform: translateX(-50%); white-space: nowrap;
  }
  .row-number {
    position: absolute; left: 996px; font-family: "Arimo", Arial, sans-serif;
    font-size: 13px; color: var(--ink);
  }
  .card {
    position: absolute; width: 394px; height: 212px;
    border: 1px solid var(--card-border); background: var(--paper); overflow: hidden;
  }
  .card--front { left: 27px; }
  .card--back { left: 547px; }
  .card--filled { background: var(--brand-blue); border-color: var(--brand-blue); }

  .wordmark {
    position: absolute; display: flex; align-items: center; gap: 10px;
    transform: translateY(-50%); color: var(--brand-blue);
    font-weight: 400; font-size: 25px; white-space: nowrap;
  }
  .wordmark__dot { width: 14px; height: 14px; border-radius: 50%; background: var(--brand-blue); flex: none; }
  .wordmark--small { font-size: 20px; gap: 8px; }
  .wordmark--small .wordmark__dot { width: 11px; height: 11px; }

  .accent-band {
    position: absolute; left: 0; right: 0; top: 170px; height: 12px; display: flex;
  }
  .accent-band__solid { width: 131px; background: var(--brand-blue); }
  .accent-band__ticks {
    flex: 1; margin-left: 5px; margin-right: 5px;
    background: repeating-linear-gradient(90deg, var(--brand-blue) 0 3px, transparent 3px 6px);
  }

  .contact, .identity { position: absolute; white-space: nowrap; }
  .contact { font-size: 14.5px; line-height: 18px; color: var(--text-grey); }
  .identity { font-size: 17px; line-height: 21px; color: var(--text-grey); }
  .identity__name { color: var(--brand-blue); }
  .on-blue, .on-blue .identity__name { color: var(--paper); }

  .side-panel { position: absolute; left: 0; top: 0; bottom: 0; width: 190px; background: var(--brand-blue); }
  .divider { position: absolute; width: 2px; background: var(--brand-blue); }
</style>
</head>
<body>
<main class="sheet">
  <span class="sheet-label" style="left:237px;top:14px">front</span>
  <span class="sheet-label" style="left:732px;top:14px">back</span>
  <span class="sheet-label" style="left:237px;top:276px">9cm x5cm Height</span>
  <span class="sheet-label" style="left:732px;top:276px">9cm x5cm Height</span>

  <!-- Option 1 -->
  <section class="card card--front" style="top:46px">
    <div class="wordmark" style="left:20px;top:79px"><span class="wordmark__dot"></span>Meridian Care Partners</div>
    <div class="accent-band"><div class="accent-band__solid"></div><div class="accent-band__ticks"></div></div>
  </section>
  <section class="card card--back card--filled" style="top:46px">
    <div class="contact on-blue" style="left:22px;top:55px">7, Lindengrove Street<br>548210 AL<br>Tel:00 031 062 047<br>fax: 00 031 062 048<br>email:info@mcp.com<br>www.mcp.com</div>
    <div class="identity on-blue" style="left:233px;top:56px"><span class="identity__name">Daniel Hollis</span><br>Sales Department</div>
  </section>
  <span class="row-number" style="top:125px">1</span>

  <!-- Option 2 -->
  <section class="card card--front" style="top:349px">
    <div class="wordmark" style="left:22px;top:101px"><span class="wordmark__dot"></span>Meridian Care Partners</div>
  </section>
  <section class="card card--back" style="top:349px">
    <div class="side-panel"></div>
    <div class="contact on-blue" style="left:22px;top:51px">7, Lindengrove Street<br>548210 AL<br>Tel:00 031 062 047<br>fax: 00 031 062 048<br>email:info@mcp.com<br>www.mcp.com</div>
    <div class="identity" style="left:233px;top:51px"><span class="identity__name">Daniel Hollis</span><br>Sales Department</div>
  </section>
  <span class="row-number" style="top:448px">2</span>

  <!-- Option 3 -->
  <section class="card card--front" style="top:656px">
    <div class="wordmark" style="left:22px;top:102px"><span class="wordmark__dot"></span>Meridian Care Partners</div>
  </section>
  <section class="card card--back" style="top:656px">
    <div class="contact" style="left:22px;top:63px">7, Lindengrove Street<br>548210 AL<br>Tel:00 031 062 047<br>fax: 00 031 062 048</div>
    <div class="divider" style="left:167px;top:58px;height:83px"></div>
    <div class="identity" style="left:202px;top:83px"><span class="identity__name">Daniel Hollis</span><br>Sales Department</div>
    <div class="contact" style="left:31px;top:175px">email:info@mcp.com</div>
    <div class="contact" style="left:203px;top:175px">www.mcp.com</div>
  </section>
  <span class="row-number" style="top:730px">3</span>

  <!-- Option 4 -->
  <section class="card card--front" style="top:958px">
    <div class="wordmark wordmark--small" style="left:110px;top:148px"><span class="wordmark__dot"></span>Meridian Care Partners</div>
  </section>
  <section class="card card--back" style="top:958px">
    <div class="identity" style="left:37px;top:35px"><span class="identity__name">Daniel Hollis</span><br>Sales Department</div>
    <div class="contact" style="left:232px;top:79px">7, Lindengrove Street<br>548210 AL<br>Tel:00 031 062 047<br>fax: 00 031 062 048<br>email:info@mcp.com<br>www.mcp.com</div>
  </section>
  <span class="row-number" style="top:1047px">4</span>
</main>
</body>
</html>
```